Letterhead design - Harwick Group

We have just had our Logo created and our now wantng a letterhead design to incorporate this. Please use the same colours as in the logo, which is attached.
Please use the company details below
P O Box 86, Kelmarsh 7315
Ph: 03 642 1937
dave@harwickgroup.co.nz
We would like a professional look
We need an overall letterhead design for our varied group of buisinesses which are based in NZ and overseas. We grow and develop buisinesses. Our companies began in NZ but we now have branches overseas as well. People are our greatest asset and we employ some incredible staff. Our buisinesses are scientific, innovative and growing in size and expertise with a financial base.

Target Market(s)

Professionals

Industry/Entity Type

Investment

Requirements
Must have
• Easy to read.
• Please use the same colours as in the logo
• Please use the company details below
• P O Box 86, Kelmarsh 7315
• Ph: 03 642 1937
• dave@harwickgroup.co.nz

```html
<!DOCTYPE html>
<html lang="en">
<head>
<meta charset="utf-8">
<title>Harwick Group Letterhead</title>
<link href="https://fonts.googleapis.com/css2?family=Montserrat:wght@500;700&family=Questrial&display=swap" rel="stylesheet">
<style>
  :root {
    --backdrop: #ddd0bb;
    --paper: #ffffff;
    --brand-green: #1fb474;
    --brand-grey: #58595b;
    --ink: #3a3a3a;
    --ink-soft: #7a7a7a;
  }
  * { box-sizing: border-box; margin: 0; padding: 0; }
  html, body {
    width: 1200px; height: 899px; overflow: hidden;
    background: var(--backdrop);
  }
  .letterhead {
    position: absolute; left: 296px; top: 20px;
    width: 608px; height: 860px;
    background: var(--paper);
    box-shadow: 0 6px 24px rgba(0,0,0,0.18);
    font-family: "Questrial", sans-serif;
    color: var(--ink);
  }
  .brand {
    position: absolute; top: 62px; left: 0; right: 0;
    display: flex; justify-content: center; align-items: center; gap: 12px;
  }
  .brand-mark { width: 34px; height: 34px; background: var(--brand-grey); }
  .brand-name {
    font-family: "Montserrat", sans-serif; font-weight: 700;
    font-size: 30px; letter-spacing: 1px; color: var(--brand-green);
    text-transform: uppercase;
  }
  .header-rule {
    position: absolute; left: 0; right: 0; top: 132px;
    height: 4px; background: var(--brand-grey);
  }
  .header-band {
    position: absolute; left: 0; right: 0; top: 140px; height: 24px;
    background: var(--brand-green);
    display: flex; align-items: center; justify-content: center;
  }
  .website {
    font-family: "Montserrat", sans-serif; font-weight: 500;
    font-size: 12px; letter-spacing: 2px; color: #fff; text-transform: uppercase;
  }
  .letter-body {
    position: absolute; left: 94px; top: 230px; width: 420px;
    font-size: 11.5px; line-height: 1.75; text-align: justify;
  }
  .letter-body p + p { margin-top: 18px; }
  .signature { position: absolute; right: 94px; top: 612px; }
  .signature-name { font-size: 13px; color: var(--ink); }
  .signature-role { font-size: 9px; color: var(--ink-soft); margin-top: 2px; }
  .footer-rule { position: absolute; left: 0; right: 0; height: 3px; background: var(--brand-green); }
  .footer-rule.top { top: 742px; }
  .footer-rule.bottom { top: 782px; }
  .footer-band {
    position: absolute; left: 0; right: 0; top: 749px; height: 29px;
    background: var(--brand-grey);
    display: flex; align-items: center; justify-content: space-around;
    padding: 0 60px;
  }
  .contact {
    font-family: "Montserrat", sans-serif; font-weight: 500;
    font-size: 11.5px; color: #fff; letter-spacing: 0.3px; white-space: nowrap;
  }
  .footer-base {
    position: absolute; left: 0; right: 0; top: 789px; height: 18px;
    background: var(--brand-grey);
  }
</style>
</head>
<body>
  <main class="letterhead">
    <header>
      <div class="brand">
        <span class="brand-mark" aria-hidden="true"></span>
        <span class="brand-name">Harwick Group</span>
      </div>
      <div class="header-rule"></div>
      <div class="header-band"><span class="website">harwickgroup.co.nz</span></div>
    </header>

    <section class="letter-body">
      <p>Thank you for your recent enquiry regarding our group services. We have reviewed your request and are pleased to confirm that our team can assist with the planning, funding and growth of your business. Our advisers will contact you within the coming week to arrange a meeting at a time that suits you. In the meantime, please find attached a short summary of the services we offer across New Zealand and overseas.</p>
      <p>Our businesses are scientific, innovative and growing in size and expertise. We invest in people first, and we are proud of the staff who make each of our companies succeed. We look forward to learning more about your goals and how we can support them.</p>
      <p>Should you have any questions before our meeting, please do not hesitate to contact our office by phone or email. We value every new partnership and aim to respond to all enquiries promptly. Thank you again for considering our group, and we look forward to working with you.</p>
    </section>

    <div class="signature">
      <div class="signature-name">Liam Carver</div>
      <div class="signature-role">Co-Founder &amp; CEO</div>
    </div>

    <footer>
      <div class="footer-rule top"></div>
      <div class="footer-band">
        <span class="contact">03 642 1937</span>
        <span class="contact">dave@harwickgroup.co.nz</span>
        <span class="contact">P O Box 86, Kelmarsh 7315</span>
      </div>
      <div class="footer-rule bottom"></div>
      <div class="footer-base"></div>
    </footer>
  </main>
</body>
</html>
```